Business Card Design Project

I need some business cards with the logo you did for us (attached)
I am looking for a coulourful yet serious business card

We do market research
on the back I want the logo

on the front my name : Corinne Vasseur
position : Manager
address : Plume Analytics Sarl - 24 Rue des tilleuls
1285 Bellerive - Switzerland
corinne.vasseur@plumeanalytics.ch
Tel : +4122 555 04 87
Mob France :+33 655 52 8014
Mob Italy +39 345 550 2876

The tree of the logo could also be used alone

THE BACKGROUND COLOR ON THE FRONT HAS TO BE WHITE, ON THE BACK YU CAN TRY OHER COLOUR BUT HOMOGENEOUS (NOT EXPENSIVE TO PRINT)

Target Market(s)

multinational companies or other market research companies

Industry/Entity Type

Market Research

Requirements
Must have
• logo on the back
and all the info above

```html
<!DOCTYPE html>
<html lang="en">
<head>
<meta charset="utf-8">
<title>Plume Analytics – Business Cards</title>
<link href="https://fonts.googleapis.com/css2?family=Arimo:wght@400;700&display=swap" rel="stylesheet">
<style>
  :root {
    --canvas: #ffffff;
    --card-border: #3a3a3a;
    --ink: #222222;
    --brand: #c4254f;
    --brand-deep: #c22a58;
    --brand-soft: #d45a80;
    --ghost: #f1eeee;
    --white: #ffffff;
  }
  * { margin: 0; padding: 0; box-sizing: border-box; }
  html, body {
    width: 1200px; height: 1019px; overflow: hidden;
    background: var(--canvas);
    font-family: "Arimo", Arial, sans-serif;
  }
  .sheet { position: relative; width: 1200px; height: 1019px; }
  .card {
    position: absolute; width: 591px; height: 327px;
    border: 1.5px solid var(--card-border);
    background: var(--white); overflow: hidden;
  }
  .col-front { left: 2px; }
  .col-back { left: 607px; }
  .row-1 { top: 2px; }
  .row-2 { top: 344px; }
  .row-3 { top: 688px; }

  .holder-name { position: absolute; font-weight: 700; font-size: 21px; color: var(--ink); white-space: nowrap; }
  .holder-role { position: absolute; font-size: 11.5px; color: var(--brand); }
  .brand-name { position: absolute; color: var(--brand); font-weight: 400; white-space: nowrap; letter-spacing: -0.5px; }
  .brand-small { font-size: 30px; }
  .contact {
    position: absolute; right: 24px; top: 178px;
    text-align: right; font-size: 14.5px; line-height: 20px; color: var(--brand);
  }
  .contact .phones { margin-top: 12px; }

  .back-brand {
    position: absolute; left: 0; right: 0; top: 168px;
    text-align: center; font-size: 66px; letter-spacing: -1px; white-space: nowrap;
  }
  .back-solid { background: var(--brand-deep); border-color: var(--brand-deep); }
  .back-solid .back-brand { color: var(--brand-soft); }
  .back-glow {
    background: radial-gradient(ellipse 55% 60% at 50% 50%, #ffffff 0%, #f3c6d3 40%, var(--brand-deep) 100%);
    border-color: var(--brand-deep);
  }
  .back-glow .back-brand { color: var(--brand); }
  .back-white .back-brand { color: var(--brand); }

  .ghost-brand {
    position: absolute; left: 12px; top: 218px;
    font-size: 96px; color: var(--ghost); white-space: nowrap; letter-spacing: -2px;
  }
</style>
</head>
<body>
<div class="sheet">

  <!-- Row 1 -->
  <section class="card col-front row-1">
    <div class="holder-name" style="left:28px; top:96px;">Corinne Vasseur</div>
    <div class="holder-role" style="left:96px; top:124px;">Manager</div>
    <div class="brand-name brand-small" style="right:30px; top:88px;">plume analytics</div>
    <div class="contact">
      <p>Plume Analytics Sarl - 24 Rue des tilleuls</p>
      <p>1285 Bellerive - Switzerland</p>
      <p>corinne.vasseur@plumeanalytics.ch</p>
      <div class="phones">
        <p>Tel : +4122 555 04 87</p>
        <p>Mob France :+33 655 52 8014</p>
        <p>Mob Italy +39 345 550 2876</p>
      </div>
    </div>
  </section>
  <section class="card col-back row-1 back-white">
    <div class="brand-name back-brand">plume analytics</div>
  </section>

  <!-- Row 2 -->
  <section class="card col-front row-2">
    <div class="brand-name brand-small" style="left:30px; top:92px;">plume analytics</div>
    <div class="holder-name" style="right:24px; top:100px;">Corinne Vasseur</div>
    <div class="holder-role" style="right:24px; top:128px;">Manager</div>
    <div class="contact">
      <p>Plume Analytics Sarl - 24 Rue des tilleuls</p>
      <p>1285 Bellerive - Switzerland</p>
      <p>corinne.vasseur@plumeanalytics.ch</p>
      <div class="phones">
        <p>Tel : +4122 555 04 87</p>
        <p>Mob France :+33 655 52 8014</p>
        <p>Mob Italy +39 345 550 2876</p>
      </div>
    </div>
  </section>
  <section class="card col-back row-2 back-solid">
    <div class="brand-name back-brand">plume analytics</div>
  </section>

  <!-- Row 3 -->
  <section class="card col-front row-3">
    <div class="brand-name ghost-brand" aria-hidden="true">plume analytics</div>
    <div class="holder-name" style="left:28px; top:100px;">Corinne Vasseur</div>
    <div class="holder-role" style="left:96px; top:128px;">Manager</div>
    <div class="brand-name brand-small" style="right:30px; top:92px;">plume analytics</div>
    <div class="contact">
      <p>Plume Analytics Sarl - 24 Rue des tilleuls</p>
      <p>1285 Bellerive - Switzerland</p>
      <p>corinne.vasseur@plumeanalytics.ch</p>
      <div class="phones">
        <p>Tel : +4122 555 04 87</p>
        <p>Mob France :+33 655 52 8014</p>
        <p>Mob Italy +39 345 550 2876</p>
      </div>
    </div>
  </section>
  <section class="card col-back row-3 back-glow">
    <div class="brand-name back-brand">plume analytics</div>
  </section>

</div>
</body>
</html>
```